The Perfect Business Card for Vantorell

I am looking for a business card which beautifully incorporates my logo, reflects my business and looks special, elegant and clean.

```html
<!DOCTYPE html>
<html lang="en">
<head>
<meta charset="utf-8">
<title>Vantorell Business Card</title>
<link rel="stylesheet" href="https://fonts.googleapis.com/css2?family=Marcellus&family=Philosopher&family=Roboto:wght@300&family=Caveat:wght@500&display=swap">
<style>
  :root {
    --backdrop: #2b2b2b;
    --card: #222325;
    --card-edge: #2c2d30;
    --green: #6a8a36;
    --green-band: #4f6b2b;
    --white: #eeeeee;
    --emboss: #141414;
    --emboss-light: #3a3b3e;
  }
  * { margin: 0; padding: 0; box-sizing: border-box; }
  html, body { width: 1200px; height: 1138px; overflow: hidden; }
  body { background: var(--backdrop); position: relative; }

  .card {
    position: absolute;
    width: 620px;
    height: 375px;
    border-radius: 16px;
    background: linear-gradient(160deg, #1d1e20 0%, var(--card) 55%, var(--card-edge) 100%);
    overflow: hidden;
  }
  .card--front { left: 272px; top: 184px; }
  .card--back { left: 274px; top: 606px; }

  .front-mark {
    position: absolute; left: 92px; top: 112px;
    display: flex; align-items: center; gap: 22px;
  }
  .mark-circle {
    width: 122px; height: 122px; border-radius: 50%;
    border: 2px solid var(--emboss);
  }
  .front-name {
    font-family: "Marcellus", serif;
    font-size: 60px; letter-spacing: 1px;
    color: var(--emboss);
    text-shadow: 0 1px 0 var(--emboss-light);
  }

  .back-mark {
    position: absolute; left: 38px; top: 110px;
    display: flex; align-items: center; gap: 20px;
  }
  .back-mark .mark-circle { width: 120px; height: 120px; border-color: var(--green); }
  .back-name {
    font-family: "Marcellus", serif;
    font-size: 36px; color: var(--white);
  }

  .holder {
    position: absolute; left: 339px; top: 102px;
    font-family: "Philosopher", sans-serif;
    font-size: 27px; color: var(--green);
  }
  .contacts {
    position: absolute; left: 339px; top: 168px;
    list-style: none;
    font-family: "Roboto", sans-serif; font-weight: 300;
    font-size: 17px; color: var(--white);
  }
  .contacts li { display: flex; align-items: center; gap: 16px; height: 24px; }
  .contacts svg { width: 16px; height: 16px; fill: var(--green); }

  .band { position: absolute; left: 0; bottom: 0; width: 620px; height: 45px; }
  .tagline {
    position: absolute; left: 350px; bottom: 8px;
    font-family: "Caveat", cursive; font-size: 26px; color: var(--white);
  }
</style>
</head>
<body>
  <section class="card card--front">
    <div class="front-mark">
      <span class="mark-circle"></span>
      <span class="front-name">Vantorell</span>
    </div>
  </section>

  <section class="card card--back">
    <div class="back-mark">
      <span class="mark-circle"></span>
      <span class="back-name">Vantorell</span>
    </div>

    <p class="holder">Marlene Hostetter</p>
    <ul class="contacts">
      <li>
        <svg viewBox="0 0 16 16" aria-hidden="true"><path d="M2 5c0-2 3-3 6-3s6 1 6 3v1h-3V5H5v1H2zM4 7h8l2 6H2z"/></svg>
        000-0000-0000
      </li>
      <li>
        <svg viewBox="0 0 16 16" aria-hidden="true"><path d="M1 3h14v10H1zM2.5 4.5 8 9l5.5-4.5v1L8 10 2.5 5.5z" fill-rule="evenodd"/></svg>
        marlene@vantorell.com
      </li>
      <li>
        <svg viewBox="0 0 16 16" aria-hidden="true"><circle cx="8" cy="8" r="6.5"/><path d="M1.5 8h13M8 1.5v13M3 4.5h10M3 11.5h10" stroke="#222325" stroke-width="1" fill="none"/></svg>
        www.vantorell.com
      </li>
    </ul>

    <svg class="band" viewBox="0 0 620 45" aria-hidden="true">
      <rect x="0" y="31" width="620" height="14" fill="var(--green-band)"/>
      <polygon points="290,0 620,0 620,45 268,45" fill="var(--green-band)"/>
    </svg>
    <p class="tagline">Live your best life</p>
  </section>
</body>
</html>
```